Airborne Sensor Mfr Needs New Backdrop for Exhibition Booth

Our company manufacturers airborne hyperspectral and thermal cameras installed on drones and aircraft. Our customers work in numerous fields from forestry to oceanography, and from defense to oil & gas. We will be attending an airborne survey and mapping conference in a few months and want to try a new backdrop for the booth which will be about 3m x 3m. We are looking for something new and fresh with a high-tech but simple feel, professional and established but also friendly and inviting. Please see my below primitive draft design for some suggested text, images, and icons that I have in mind. Can you turn this into something really compelling that draws people to our booth? Or do you have some new ideas to build on my design? Look forward to seeing what you can do!
https://pelvaq.com/

```html
<!DOCTYPE html>
<html lang="en">
<head>
<meta charset="utf-8">
<title>Pelvaq Airborne Sensors – Booth Backdrop</title>
<link rel="stylesheet" href="https://fonts.googleapis.com/css2?family=Lexend:wght@400;500;600&family=Orbitron:wght@800;900&display=swap">
<style>
  :root {
    --navy-deep: #0b1528;
    --navy: #13284a;
    --navy-mid: #1a3558;
    --panel: #182b48;
    --panel-edge: #2d4a70;
    --white: #f2f4f8;
    --label: #e6ebf2;
    --wave-blue: rgba(59,143,224,.28);
    --wave-pink: rgba(217,67,110,.28);
    --wave-orange: rgba(240,138,36,.32);
    --tile-blue: #2f7fd6;
    --tile-pink: #c83c7a;
    --tile-yellow: #f3d34a;
  }
  * { box-sizing: border-box; margin: 0; padding: 0; }
  html, body { width: 1163px; height: 1200px; overflow: hidden; background: var(--navy-deep); }
  .backdrop {
    position: relative; width: 1163px; height: 1200px; overflow: hidden;
    background: radial-gradient(ellipse at 50% 35%, var(--navy-mid) 0%, var(--navy) 45%, var(--navy-deep) 100%);
    font-family: "Lexend", sans-serif; color: var(--white);
  }
  .header-glow {
    position: absolute; left: 0; top: 20px; width: 1163px; height: 190px;
    background:
      radial-gradient(ellipse 32% 45% at 12% 45%, var(--wave-blue) 0%, transparent 100%),
      radial-gradient(ellipse 30% 45% at 55% 35%, var(--wave-pink) 0%, transparent 100%),
      radial-gradient(ellipse 25% 50% at 92% 55%, var(--wave-orange) 0%, transparent 100%);
  }
  .brand {
    position: absolute; top: 92px; left: 0; width: 100%;
    display: flex; justify-content: center; align-items: center; gap: 26px;
    font-family: "Lexend", sans-serif; font-weight: 600; font-size: 66px; line-height: 1; white-space: nowrap;
  }
  .brand-divider { width: 2px; height: 70px; background: var(--white); opacity: .8; }
  .drone-photo {
    position: absolute; left: 208px; top: 228px; width: 748px; height: 240px;
    border-radius: 40% 40% 30% 30% / 30% 30% 60% 60%;
    background: radial-gradient(ellipse at 50% 45%, #d9dde3 0%, #5d6674 28%, #1d2a3e 60%, transparent 75%);
    opacity: .9;
  }
  .panel { position: absolute; left: 0; top: 450px; width: 1163px; height: 750px; }
  .headline {
    position: absolute; top: 500px; left: 0; width: 100%; text-align: center; white-space: nowrap;
    font-family: "Orbitron", sans-serif; font-weight: 900; font-size: 57px; line-height: 68px; letter-spacing: 1px;
  }
  .focus-grid {
    position: absolute; left: 100px; top: 674px; width: 972px;
    display: grid; grid-template-columns: repeat(6, 162px); grid-auto-rows: 204px; list-style: none;
  }
  .focus-item { display: flex; flex-direction: column; align-items: center; }
  .tile {
    flex-shrink: 0;
    width: 117px; height: 117px; border-radius: 10px; padding: 2px;
    background: linear-gradient(135deg, var(--tile-blue) 0%, var(--tile-pink) 50%, var(--tile-yellow) 100%);
  }
  .tile-inner {
    width: 100%; height: 100%; border-radius: 8px;
    background: linear-gradient(150deg, #2a3f5e 0%, #16243c 55%, #101c31 100%);
    display: flex; align-items: center; justify-content: center;
  }
  .tile svg { width: 62px; height: 62px; fill: none; stroke: var(--white); stroke-width: 2; stroke-linecap: round; stroke-linejoin: round; }
  .focus-label {
    margin-top: 12px; text-align: center; font-size: 19px; font-weight: 400; line-height: 24px; color: var(--label);
  }
  .particle-field {
    position: absolute; left: 0; bottom: 0; width: 1163px; height: 110px;
    background: radial-gradient(ellipse at 50% 100%, rgba(79,163,216,.55) 0%, rgba(79,163,216,.2) 45%, transparent 75%);
  }
  .particle-field-top {
    position: absolute; left: 0; top: 440px; width: 1163px; height: 70px;
    background: radial-gradient(ellipse at 50% 60%, rgba(79,163,216,.35) 0%, transparent 70%);
  }
</style>
</head>
<body>
<main class="backdrop">
  <div class="header-glow" role="img" aria-label="Decorative flowing light lines in blue, pink and orange behind the header"></div>

  <h1 class="brand"><span class="brand-name">PELVAQ</span><span class="brand-divider" aria-hidden="true"></span><span class="brand-tagline">AIRBORNE SENSORS</span></h1>

  <div class="particle-field-top" aria-hidden="true"></div>
  <div class="drone-photo" role="img" aria-label="Photo of a quadcopter drone carrying a sensor payload"></div>

  <svg class="panel" viewBox="0 0 1163 750" aria-hidden="true">
    <path d="M70 0 H1090 L1142 50 V750 H24 V50 Z" fill="none" stroke="var(--panel-edge)" stroke-width="2"/>
    <path d="M84 4 H1078 L1112 70 V750 H53 V70 Z" fill="var(--panel)" opacity=".75"/>
  </svg>

  <h2 class="headline">WHAT DO YOU WANT<br>TO DETECT AND MONITOR?</h2>

  <ul class="focus-grid">
    <li class="focus-item"><div class="tile"><div class="tile-inner">
      <svg viewBox="0 0 48 48"><path d="M6 42 V28 L14 32 V28 L22 32 V24 H28 L30 42 Z"/><path d="M28 22 a5 5 0 0 1 4-10 a6 6 0 0 1 11 3 a4 4 0 0 1-1 8 H28"/><path d="M8 20 H20 M12 16 H20"/></svg>
    </div></div><span class="focus-label">Gas Detection</span></li>
    <li class="focus-item"><div class="tile"><div class="tile-inner">
      <svg viewBox="0 0 48 48"><path d="M24 6 a8 8 0 0 1 8 8 a7 7 0 0 1 2 13 H14 a7 7 0 0 1 2-13 a8 8 0 0 1 8-8 Z"/><path d="M24 27 V42 M18 27 V42 M30 27 V42 M8 42 H40"/></svg>
    </div></div><span class="focus-label">Forestry</span></li>
    <li class="focus-item"><div class="tile"><div class="tile-inner">
      <svg viewBox="0 0 48 48"><path d="M18 10 C12 20 8 24 8 30 a10 10 0 0 0 20 0 C28 24 24 20 18 10 Z"/><path d="M32 14 C27 23 24 26 24 32 a9 9 0 0 0 18 0 C42 26 37 23 32 14 Z"/><path d="M37 30 a5 5 0 0 1-2 5"/></svg>
    </div></div><span class="focus-label">Water Quality</span></li>
    <li class="focus-item"><div class="tile"><div class="tile-inner">
      <svg viewBox="0 0 48 48"><rect x="6" y="32" width="36" height="9" rx="1"/><path d="M34 32 V10 M34 18 l-5-5 M34 18 l5-5 M34 24 l-5-4 M34 24 l5-4"/><path d="M16 32 V24 a6 6 0 0 1-6-6 a6 6 0 0 1 6 6 a6 6 0 0 1 6-6 a6 6 0 0 1-6 6"/></svg>
    </div></div><span class="focus-label">Vegetation<br>Health</span></li>
    <li class="focus-item"><div class="tile"><div class="tile-inner">
      <svg viewBox="0 0 48 48"><path d="M24 44 V10"/><path d="M24 10 c-4 3-4 7 0 9 c4-2 4-6 0-9 Z"/><path d="M24 22 c-6-2-9 2-8 6 c4 1 8-1 8-6 Z M24 22 c6-2 9 2 8 6 c-4 1-8-1-8-6 Z"/><path d="M24 32 c-6-2-9 2-8 6 c4 1 8-1 8-6 Z M24 32 c6-2 9 2 8 6 c-4 1-8-1-8-6 Z"/></svg>
    </div></div><span class="focus-label">Precision Ag</span></li>
    <li class="focus-item"><div class="tile"><div class="tile-inner">
      <svg viewBox="0 0 48 48"><circle cx="18" cy="24" r="8"/><path d="M12 30 L4 40"/><path d="M26 22 a6 6 0 0 1 10-6 a6 6 0 0 1 8 8 a5 5 0 0 1-4 9 H28"/><path d="M36 26 V44"/><circle cx="14" cy="8" r="1.5"/><circle cx="22" cy="6" r="1.5"/><circle cx="30" cy="8" r="1.5"/></svg>
    </div></div><span class="focus-label">Species<br>Classification</span></li>

    <li class="focus-item"><div class="tile"><div class="tile-inner">
      <svg viewBox="0 0 48 48"><rect x="12" y="10" width="24" height="32" rx="2"/><path d="M10 16 H38 M10 36 H38 M20 6 H28 V10"/><path d="M24 21 c-3 4-4 6-4 8 a4 4 0 0 0 8 0 c0-2-1-4-4-8 Z"/></svg>
    </div></div><span class="focus-label">Pollution /<br>Disaster<br>Response</span></li>
    <li class="focus-item"><div class="tile"><div class="tile-inner">
      <svg viewBox="0 0 48 48"><circle cx="24" cy="24" r="14"/><circle cx="24" cy="24" r="6"/><path d="M24 4 V10 M24 38 V44 M4 24 H10 M38 24 H44"/></svg>
    </div></div><span class="focus-label">Target<br>Detection</span></li>
    <li class="focus-item"><div class="tile"><div class="tile-inner">
      <svg viewBox="0 0 48 48"><path d="M12 38 a7 7 0 0 1 0-14 a10 10 0 0 1 19-4 a8 8 0 0 1 6 18 Z"/><circle cx="8" cy="14" r="2.5"/><circle cx="40" cy="10" r="3"/><text x="14" y="34" font-family="Lexend, sans-serif" font-size="10" fill="#f2f4f8" stroke="none">CO2</text></svg>
    </div></div><span class="focus-label">Environmental<br>Monitoring</span></li>
    <li class="focus-item"><div class="tile"><div class="tile-inner">
      <svg viewBox="0 0 48 48"><path d="M4 20 L16 16 L30 18 L44 12 V32 L30 34 L4 34 Z"/><path d="M4 26 H20 M32 24 H44"/><circle cx="26" cy="30" r="6"/><path d="M21 34 L14 42"/></svg>
    </div></div><span class="focus-label">Geology /<br>Mineral<br>Exploration</span></li>
    <li class="focus-item"><div class="tile"><div class="tile-inner">
      <svg viewBox="0 0 48 48"><path d="M12 30 V8 a4 4 0 0 1 8 0 V30 a7 7 0 1 1-8 0 Z"/><path d="M16 14 V34"/><path d="M34 6 L44 22 H24 Z"/><path d="M34 12 V16 M34 19 V19.5"/></svg>
    </div></div><span class="focus-label">Thermal<br>Anomalies</span></li>
    <li class="focus-item"><div class="tile"><div class="tile-inner">
      <svg viewBox="0 0 48 48"><path d="M24 4 C30 14 36 20 36 28 a12 12 0 0 1-24 0 C12 20 18 14 24 4 Z"/><path d="M24 18 c3 5 6 8 6 12 a6 6 0 0 1-12 0 c0-4 3-7 6-12 Z"/><path d="M8 42 H40"/></svg>
    </div></div><span class="focus-label">Wildfire /<br>Hotspot</span></li>
  </ul>

  <div class="particle-field" aria-hidden="true"></div>
</main>
</body>
</html>
```